Retirement Community Letterhead design needed to include our new logo

We recently updated our logo and need a new letterhead to go with it. Would like the letterhead to be clean, classic, and easy to read. I've attached our current logo and a copy of our old letterhead for reference.

If possible, we would like, "Living Well Together" to be included in someway.

Ashbrook Faith Meadows is a faith-based, not-for profit senior living community offering Independent Living, Assisted Living, and a Health Care Center.

Target Market(s)

45+ Women

Industry/Entity Type

Community

Colors
00a990

Requirements
Must have
• Must be clean and elegant.
• Font used must coordinate well with the Trajan Pro font in logo
Should not have
• No crazy graphics or details.

```html
<!DOCTYPE html>
<html lang="en">
<head>
<meta charset="utf-8">
<title>Ashbrook Faith Meadows – Letterhead</title>
<link rel="stylesheet" href="https://fonts.googleapis.com/css2?family=Cinzel:wght@500;600&family=Arimo:wght@400;700&family=Tinos:wght@400;700&display=swap">
<style>
  :root {
    --teal: #00a990;
    --teal-soft: #d7efea;
    --leaf: #2e6b3a;
    --ink: #1e1e1e;
    --paper: #ffffff;
    --backdrop: #cfcfcf;
  }
  * { box-sizing: border-box; margin: 0; padding: 0; }
  html, body { width: 1200px; height: 1200px; overflow: hidden; background: var(--backdrop); }
  .letterhead {
    position: absolute; left: 167px; top: 40px;
    width: 866px; height: 1120px;
    background: var(--paper);
    box-shadow: 0 4px 18px rgba(0,0,0,.18);
    font-family: "Arimo", Arial, sans-serif;
    color: var(--ink);
    overflow: hidden;
  }
  .brand {
    position: absolute; left: 62px; top: 92px;
    display: flex; align-items: center; gap: 14px;
  }
  .brand__dot { width: 30px; height: 30px; border-radius: 50%; background: var(--leaf); flex: none; }
  .brand__name {
    font-family: "Cinzel", serif; font-weight: 600; color: var(--leaf);
    font-size: 27px; line-height: 1.05; letter-spacing: 2px; text-transform: uppercase;
  }
  .header-rule { position: absolute; left: 62px; top: 190px; width: 744px; height: 2px; background: var(--teal); }
  .contact { position: absolute; left: 560px; top: 46px; width: 246px; height: 146px; }
  .contact__bracket { position: absolute; left: 0; top: 0; }
  .contact__lines {
    position: absolute; left: 24px; top: 6px;
    font-family: "Tinos", serif; font-weight: 700; color: var(--teal);
    font-size: 13px; line-height: 1.45;
  }
  .contact__phone { display: flex; align-items: center; gap: 6px; }
  .contact__phone svg { width: 13px; height: 13px; flex: none; }
  .salutation { position: absolute; left: 62px; top: 230px; font-weight: 700; font-size: 14px; }
  .letter-body {
    position: absolute; left: 62px; top: 264px; width: 730px;
    font-size: 12.5px; line-height: 1.62;
  }
  .letter-body p + p { margin-top: 16px; }
  .closing { position: absolute; left: 62px; top: 800px; }
  .closing__phrase { font-size: 13px; }
  .closing__signature { width: 130px; height: 36px; margin: 8px 0 4px 20px; background: var(--teal-soft); border-radius: 4px; }
  .closing__name, .band__name { font-family: "Tinos", serif; font-weight: 700; font-size: 14px; color: var(--teal); }
  .closing__title, .band__title { font-family: "Tinos", serif; font-weight: 400; font-size: 11px; color: var(--teal); letter-spacing: .5px; }
  .closing__name, .closing__title { padding-left: 48px; }
  .band { position: absolute; left: 0; top: 1038px; width: 826px; height: 42px; background: var(--teal); }
  .band__motto {
    position: absolute; left: 28px; top: 10px;
    font-family: "Cinzel", serif; font-weight: 500; color: var(--paper);
    font-size: 19px; line-height: 22px; letter-spacing: 4px; text-transform: uppercase;
    white-space: nowrap;
  }
  .band__tab {
    position: absolute; left: 640px; top: 946px; width: 186px; height: 100px;
    background: var(--teal); text-align: center; padding-top: 10px;
  }
  .band__mark { width: 32px; height: 32px; border-radius: 50%; background: var(--paper); margin: 0 auto 8px; }
  .band__name, .band__title { color: var(--paper); }
</style>
</head>
<body>
<main class="letterhead">
  <header>
    <div class="brand">
      <span class="brand__dot"></span>
      <div class="brand__name">Ashbrook<br>Faith Meadows</div>
    </div>
    <div class="contact">
      <svg class="contact__bracket" width="30" height="146" viewBox="0 0 30 146">
        <path d="M18 2 C2 40 2 110 28 145" fill="none" stroke="var(--teal)" stroke-width="2"/>
      </svg>
      <div class="contact__lines">
        <div>48 Meadowlark Lane</div>
        <div>Springvale, Ohio 45012-3300</div>
        <div class="contact__phone">
          <svg viewBox="0 0 14 14"><circle cx="7" cy="7" r="6.3" fill="none" stroke="var(--ink)" stroke-width="1"/><path d="M4.5 4 L6 3.6 L6.6 5.3 L5.7 6 Q6.4 7.6 8 8.3 L8.7 7.4 L10.4 8 L10 9.5 Q6 10 4.5 4Z" fill="var(--ink)"/></svg>
          (555) 310-2746
        </div>
        <div class="contact__phone">
          <svg viewBox="0 0 14 14"><circle cx="7" cy="7" r="6.3" fill="none" stroke="var(--ink)" stroke-width="1"/><rect x="4" y="5" width="6" height="5" fill="var(--ink)"/><rect x="5" y="3" width="4" height="2.5" fill="none" stroke="var(--ink)" stroke-width=".8"/></svg>
          (555) 310-8813
        </div>
      </div>
    </div>
    <div class="header-rule"></div>
  </header>

  <p class="salutation">Dear Mr. ABCD</p>
  <section class="letter-body">
    <p>Thank you for your recent interest in our community. For more than forty years our campus has welcomed older adults who value comfort, friendship and a life shaped by faith. Our residents enjoy quiet walking paths, shared meals, weekly chapel services and a calendar full of classes, outings and gatherings that keep every day bright and full of purpose.</p>
    <p>We offer three levels of living on one campus. Independent Living apartments give residents freedom with none of the chores of home ownership. Assisted Living adds a gentle hand with daily tasks, medication and meals, while our Health Care Center provides skilled nursing and rehabilitation by a caring, experienced staff who know each resident by name.</p>
    <p>As a not-for-profit ministry, every gift and every fee is returned to the care of our residents. We are grateful for friends like you who help us keep that promise year after year.</p>
    <p>We would be delighted to show you around in person. Tours are offered each weekday morning and afternoon, and our team is glad to answer questions about floor plans, services, dining and costs. Please bring family members along, since choosing a new home is a decision best shared.</p>
    <p>Enclosed you will find our latest brochure along with a schedule of upcoming open house events. If you have any questions before your visit, please call our office at the number listed above. We look forward to meeting you and welcoming you into the warm community we are proud to share.</p>
  </section>

  <div class="closing">
    <p class="closing__phrase">Sincerely Yours,</p>
    <div class="closing__signature" role="img" aria-label="Handwritten signature of the executive director"></div>
    <p class="closing__name">Daniel Whitford</p>
    <p class="closing__title">Executive Director</p>
  </div>

  <footer>
    <div class="band__tab">
      <div class="band__mark"></div>
      <p class="band__name">Daniel Whitford</p>
      <p class="band__title">Executive Director</p>
    </div>
    <div class="band"><span class="band__motto">Living Well Together</span></div>
  </footer>
</main>
</body>
</html>
```